Etiketten für Kosmetik Produkte  100% Natural Made in Germany
Etiketten für Kosmetik Produkte 100% Natural Made in Germany
Zielgruppe
auf Hochwertige -zertifizierte Naturprodukte wert legen.
Hergestellt in Deutschland und Verpackt
Aufgabenstellung
Hallo ihr lieben,
für die SilbTau Kosmetik - wünschen wir einen neuen frischen Style - das dunkle Etikett möchten wir los werden.
Ein helles frisches Design
Zielgruppe- alle die auf Hochwertige - zertifizierte Naturprodukte bevorzugen
Die Produkte haben mit eine VERUN Zertifizierung - Höchste Qalität an Naturprodukte
Das Glas was wir nutzen ist ein violettes Glas und sehr hochwertig was wir beibehalten möchten.
Das Produkt ist dadurch sehr Geschütz und nachhaltig dazu
Es sind 12 Produkte - Design bleibt bei allen gleich.
Design Wunsch -!!!!
Was gut zum Glas Passt- nur kein schwarz bitte
und Produkt gut passt
Weiß - Kupfer eventuell
Kein Muss - sind für alles offen ( nur kein schwarz
Logo - Name bleibt :-)
Das Design von Tesoro Naturkosmetik
Gefällt uns sehr gut in der Richtung
Was die Natürlichkeit- Reinheit - Qualität
Verkörpert:-)
Fotos zum Prosukt:
Hier ein link zum Instagram
https://instagram.com/lumaroze.spain?igshid=MzRlODBiNWFlZA==
https://instagram.com/silbtau_naturkosmetik?igshid=MzRlODBiNWFlZA==
An den Flyer den wir hochgeladen kann man sehen um welche Produkte es sich handelt und auch im Instagram zu sehen sind.
Wenn ihr weitere Fotos benötigen tut- bitte melden
Viel Glück :-) danke für eure Unterstützung

```html
<!DOCTYPE html>
<html lang="de">
<head>
<meta charset="utf-8">
<title>SilbTau Naturkosmetik – Allrounder Cream Etikett</title>
<link rel="stylesheet" href="https://fonts.googleapis.com/css2?family=Montserrat:wght@400;500;700&display=swap">
<style>
  :root {
    --glass-violet: #1c0748;
    --label-cream: #e4dccf;
    --copper: #9a6a2c;
    --copper-soft: #b07c3a;
  }
  html, body {
    margin: 0;
    padding: 0;
    width: 1200px;
    height: 1200px;
    overflow: hidden;
    background: var(--glass-violet);
  }
  .label {
    position: relative;
    width: 1200px;
    height: 1200px;
    font-family: "Montserrat", sans-serif;
  }
  .label-art {
    position: absolute;
    inset: 0;
  }
  .text-block {
    position: absolute;
    left: 0;
    width: 1200px;
    text-align: center;
    color: var(--copper);
    margin: 0;
    line-height: 1;
  }
  .brand-name {
    top: 514px;
    font-size: 60px;
    font-weight: 500;
    letter-spacing: 4px;
  }
  .brand-sub {
    top: 572px;
    font-size: 30px;
    font-weight: 500;
    letter-spacing: 2px;
  }
  .product-name {
    top: 664px;
    left: -12px;
    font-size: 33px;
    font-weight: 700;
    letter-spacing: 2px;
  }
  .category {
    top: 939px;
    left: 11px;
    font-size: 31px;
    font-weight: 700;
    letter-spacing: 1.5px;
  }
  .quality {
    top: 984px;
    font-size: 23px;
    font-weight: 400;
    letter-spacing: 1.5px;
  }
</style>
</head>
<body>
<main class="label">
  <svg class="label-art" width="1200" height="1200" viewBox="0 0 1200 1200" xmlns="http://www.w3.org/2000/svg">
    <defs>
      <clipPath id="label-shape">
        <circle cx="600" cy="600" r="570"/>
      </clipPath>
      <radialGradient id="pattern-glow-top" cx="0.75" cy="0.35" r="0.6">
        <stop offset="0" stop-color="#b07c3a" stop-opacity="0.28"/>
        <stop offset="1" stop-color="#b07c3a" stop-opacity="0"/>
      </radialGradient>
      <radialGradient id="pattern-glow-bottom" cx="0.3" cy="0.7" r="0.6">
        <stop offset="0" stop-color="#b07c3a" stop-opacity="0.28"/>
        <stop offset="1" stop-color="#b07c3a" stop-opacity="0"/>
      </radialGradient>
    </defs>
    <circle class="label-disc" cx="600" cy="600" r="570" fill="var(--label-cream)"/>
    <g clip-path="url(#label-shape)">
      <rect class="pattern-area pattern-top" role="img" aria-label="Kupferfarbenes geometrisches Linien- und Punktnetz oben rechts" x="460" y="30" width="720" height="660" fill="url(#pattern-glow-top)"/>
      <rect class="pattern-area pattern-bottom" role="img" aria-label="Kupferfarbenes geometrisches Linien- und Punktnetz unten links" x="20" y="570" width="660" height="620" fill="url(#pattern-glow-bottom)"/>
    </g>
    <circle class="brand-mark" cx="598" cy="461" r="45" fill="none" stroke="var(--copper)" stroke-width="2"/>
  </svg>

  <p class="text-block brand-name">SILBTAU</p>
  <p class="text-block brand-sub">NATURKOSMETIK</p>
  <h1 class="text-block product-name">ALLROUNDER CREAM</h1>
  <p class="text-block category">FACIAL CARE</p>
  <p class="text-block quality">ORGANIC</p>
</main>
</body>
</html>
```